Business Card Design Project

We are a construction company in Orange County, CA. We need a two sided business card. We would like the back to be our logo with web URL. Front should included Name, title, address, phone, fax and email address.

our address is
627 West Marrow Blvd, Suite 305
Fairhaven, CA 90417

Our logo files are attached.

Construction

```html
<!DOCTYPE html>
<html lang="en">
<head>
<meta charset="utf-8">
<title>Braxel Business Card</title>
<link href="https://fonts.googleapis.com/css2?family=Source+Sans+3:ital,wght@0,400;0,600;0,700;1,700&display=swap" rel="stylesheet">
<style>
  :root {
    --brand-blue: #134b7c;
    --accent-grey: #b4b6b9;
    --text-dark: #3b3b3b;
    --card-white: #ffffff;
    --backdrop: #e4e5e7;
  }
  * { margin: 0; padding: 0; box-sizing: border-box; }
  html, body { width: 960px; height: 1200px; overflow: hidden; }
  body {
    background: var(--backdrop);
    font-family: "Source Sans 3", Arial, sans-serif;
    color: var(--text-dark);
    position: relative;
  }
  .card {
    position: absolute;
    width: 840px;
    height: 480px;
    background: var(--card-white);
    border-radius: 28px;
    overflow: hidden;
    box-shadow: 0 4px 10px rgba(0,0,0,0.25);
    text-align: center;
  }
  .card--front { left: 55px; top: 100px; }
  .card--back { left: 60px; top: 644px; }
  .card__accent { position: absolute; left: 0; top: 0; }
  .wordmark {
    position: absolute;
    left: 0; right: 0;
    font-weight: 700;
    color: var(--brand-blue);
    line-height: 1;
    letter-spacing: 2px;
  }
  .card--front .wordmark { top: 88px; font-size: 140px; }
  .card--back .wordmark { top: 150px; font-size: 170px; }
  .contact { position: absolute; left: 0; right: 0; top: 286px; }
  .contact__name { font-size: 26px; font-weight: 600; line-height: 34px; }
  .contact__role { font-size: 20px; }
  .contact__lines { margin-top: 6px; }
  .contact__line { font-size: 20px; line-height: 38px; }
  .contact__label { font-weight: 700; font-style: italic; }
  .contact__sep { margin: 0 6px; }
  .card__url {
    position: absolute; left: 0; right: 0; top: 404px;
    font-size: 30px; font-weight: 700; line-height: 1;
  }
</style>
</head>
<body>
  <section class="card card--front">
    <svg class="card__accent" width="840" height="480" viewBox="0 0 840 480" aria-hidden="true">
      <path d="M760,0 L840,0 L840,70 Q820,18 760,0 Z" fill="var(--brand-blue)"/>
      <path d="M0,410 Q20,466 80,480 L0,480 Z" fill="var(--accent-grey)"/>
    </svg>
    <div class="wordmark">BRAXEL</div>
    <div class="contact">
      <p class="contact__name">Your Name, <span class="contact__role">Designation</span></p>
      <div class="contact__lines">
        <p class="contact__line"><span class="contact__label">e</span> : info@braxelbuild.com <span class="contact__sep">|</span> <span class="contact__label">w</span> : www.braxelbuild.com</p>
        <p class="contact__line"><span class="contact__label">p</span> : 1-234-4567 <span class="contact__sep">|</span> <span class="contact__label">f</span> : 1-234-4567</p>
        <p class="contact__line">627 West Marrow Blvd, Suite 305, Fairhaven, CA 90417</p>
      </div>
    </div>
  </section>

  <section class="card card--back">
    <div class="wordmark">BRAXEL</div>
    <p class="card__url">www.braxelbuild.com</p>
  </section>
</body>
</html>
```